Need Letterhead and Business Card

I have a logo but i need new letterhead and biz cards. We are a real estate investment firm so we need very professional but also do not want to be old fashioned. We have 3 locations; Hong Kong, London and Carmel Valley California. I can provide full addresses if needed. If you have adjustments to our logo you would recommend we are open to them.
I will be putting in a separate project but we also need a template for our own powerpoint slide presentations and website.

Real Estate

```html
<!DOCTYPE html>
<html lang="en">
<head>
<meta charset="utf-8">
<title>Halden Letterhead</title>
<link rel="stylesheet" href="https://fonts.googleapis.com/css2?family=Didact+Gothic&family=Lato:wght@400;700&display=swap">
<style>
  :root {
    --bg: #e9ecee;
    --paper: #ffffff;
    --paper-back: #f4f4f4;
    --brand-blue: #1f4f8f;
    --brand-gold: #c9a13f;
    --ink: #3a3a3a;
    --ink-soft: #555;
    --map-tone: #eef1f4;
    --mark-grey: #9a9a9a;
  }
  * { box-sizing: border-box; margin: 0; padding: 0; }
  html, body { width: 1200px; height: 924px; overflow: hidden; }
  body {
    background: var(--bg);
    font-family: "Didact Gothic", "Century Gothic", sans-serif;
    color: var(--ink);
    position: relative;
  }
  .sheet {
    position: absolute;
    top: 45px;
    width: 512px;
    height: 697px;
    border-radius: 12px;
    overflow: hidden;
  }
  .sheet--front { left: 43px; background: var(--paper); }
  .sheet--back { left: 635px; background: var(--paper-back); }

  .brand {
    position: absolute;
    left: 0; right: 0;
    text-align: center;
  }
  .brand__name {
    font-family: "Lato", sans-serif;
    font-weight: 700;
    color: var(--brand-blue);
    letter-spacing: 1px;
    line-height: 1;
  }
  .brand__tagline {
    font-family: "Lato", sans-serif;
    color: var(--brand-gold);
    text-transform: uppercase;
    letter-spacing: 0.3px;
  }
  .letterhead__brand { top: 30px; }
  .letterhead__brand .brand__name { font-size: 44px; }
  .letterhead__brand .brand__tagline { font-size: 7.5px; margin-top: 8px; }

  .letterhead__rule {
    position: absolute;
    left: 44px; right: 42px; top: 108px;
    height: 1.5px;
    background: var(--brand-gold);
  }
  .contact-row {
    position: absolute;
    left: 44px; right: 38px; top: 112px;
    display: flex;
    justify-content: space-between;
    font-size: 10.5px;
    color: var(--ink);
  }
  .contact-row__item { display: flex; align-items: center; gap: 6px; }
  .contact-row__item svg { width: 11px; height: 11px; fill: var(--brand-blue); }

  .letter-body {
    position: absolute;
    left: 44px; top: 147px;
    width: 429px;
    font-size: 11.2px;
    line-height: 17.7px;
    text-align: justify;
    hyphens: auto;
    color: var(--ink);
    z-index: 2;
  }
  .letter-body p + p { margin-top: 17.7px; }

  .faint-mark {
    position: absolute;
    left: 0; right: 0; top: 300px;
    text-align: center;
    opacity: 0.13;
    z-index: 1;
  }
  .faint-mark .brand__name { font-size: 64px; }
  .faint-mark .brand__tagline { font-size: 12px; margin-top: 6px; }

  .map-backdrop {
    position: absolute;
    left: 0; right: 0; bottom: 40px;
    height: 160px;
    background: radial-gradient(ellipse at 50% 55%, var(--map-tone) 0%, rgba(238,241,244,0.5) 55%, rgba(255,255,255,0) 80%);
    z-index: 0;
  }

  .signature {
    position: absolute;
    right: 40px; top: 572px;
    text-align: left;
    z-index: 2;
  }
  .signature__name { font-size: 13px; color: var(--ink); }
  .signature__title { font-size: 9px; color: var(--ink-soft); margin-top: 6px; }

  .locations {
    position: absolute;
    left: 60px; top: 657px;
    display: flex;
    align-items: center;
    gap: 10px;
    font-family: "Lato", sans-serif;
    font-weight: 700;
    font-size: 11.5px;
    color: var(--brand-blue);
    z-index: 2;
  }
  .locations__dot {
    width: 5px; height: 5px; border-radius: 50%;
    background: var(--brand-gold);
  }
  .footer-mark {
    position: absolute;
    right: 38px; top: 650px;
    font-family: "Lato", sans-serif;
    font-weight: 700;
    font-size: 24px;
    color: var(--mark-grey);
    z-index: 2;
  }

  .back__brand { top: 540px; }
  .back__brand .brand__name { font-size: 52px; }
  .back__brand .brand__tagline { font-size: 8.5px; margin-top: 10px; }
</style>
</head>
<body>

  <section class="sheet sheet--front" aria-label="Letterhead front">
    <div class="brand letterhead__brand">
      <div class="brand__name">HALDEN</div>
      <div class="brand__tagline">Real Estate Investment &amp; Management</div>
    </div>

    <div class="letterhead__rule"></div>

    <div class="contact-row">
      <span class="contact-row__item">
        <svg viewBox="0 0 16 16" aria-hidden="true"><path d="M3 2h3l1.5 3.5-2 1.3a8 8 0 0 0 3.7 3.7l1.3-2L14 10v3a1 1 0 0 1-1 1A11 11 0 0 1 2 3a1 1 0 0 1 1-1z"/></svg>
        +65 5550 1827
      </span>
      <span class="contact-row__item">
        <svg viewBox="0 0 16 16" aria-hidden="true"><path d="M1 3h14v10H1z M1 3l7 6 7-6" stroke="#fff" stroke-width="1"/></svg>
        info@haldenestates.com
      </span>
      <span class="contact-row__item">
        <svg viewBox="0 0 16 16" aria-hidden="true"><path d="M6.5 9.5l3-3M5 8l-2 2a2.1 2.1 0 0 0 3 3l2-2M11 8l2-2a2.1 2.1 0 0 0-3-3L8 5" fill="none" stroke="#1f4f8f" stroke-width="1.6" stroke-linecap="round"/></svg>
        www.haldenestates.com
      </span>
    </div>

    <div class="faint-mark" aria-hidden="true">
      <div class="brand__name">HALDEN</div>
      <div class="brand__tagline">Real Estate Investment &amp; Management</div>
    </div>

    <div class="map-backdrop" role="img" aria-label="Faint world map backdrop"></div>

    <div class="letter-body">
      <p>Lorem ipsum dolor sit amet, consectetur adipiscing elit. Donec orci purus, luctus vitae dignissim eu, iaculis sed purus. Vivamus faucibus, ipsum nec aliquet viverra, leo mauris condimentum ligula, sit amet sagittis enim ligula quis arcu. Nam egestas tortor id nisi porttitor mattis. In tortor ante, ultricies in suscipit a, tempus non massa. Vivamus et auctor mi. Fusce vel massa nulla. Phasellus nec eros mauris, et scelerisque orci. Donec malesuada orci vitae nulla accumsan porta a id massa.</p>
      <p>Quisque accumsan iaculis magna sit amet fringilla. Maecenas consequat, magna eget tincidunt semper, odio nibh rutrum mi, id feugiat ante nisi eu risus. Vestibulum nunc orci, rhoncus a placerat in, ultricies in mi. Cras mattis varius eros, vel fringilla nisi suscipit eget. Quisque scelerisque sagittis nulla at porttitor. Mauris a justo et tellus interdum tristique. Sed id augue vitae urna euismod commodo aliquet a quam. Pellentesque arcu velit, cursus et malesuada ut, consequat et diam. Nullam erat sem, rhoncus id ullamcorper vitae, rhoncus et arcu. In ultricies ultricies nulla,</p>
      <p>Kut rutrum nisi iaculis at. Donec eu magna a metus ornare faucibus. Fusce aliquet faucibus ultricies. Morbi semper, est id tincidunt gravida, sem arcu adipiscing lacus, ac bibendum nulla leo eu purus. Quisque nec diam sed risus consectetur a ccumsan quis quis nibh. Vestibulum id purus lorem. Donec eu magna a metus ornare faucibus. Fusce aliquet faucibus ultricies. Morbi semper, est id tincidunt gravida, sem arcu adipiscing lacus, ac bibendum nulla leo eu purus. Quisque nec diam sed risus consectetur a ccumsan quis quis nibh. Vestibulum id purus lorem.</p>
    </div>

    <div class="signature">
      <div class="signature__name">Daniel Reyes</div>
      <div class="signature__title">Co-Founder &amp; CEO</div>
    </div>

    <div class="locations">
      <span>Hong Kong</span><span class="locations__dot"></span>
      <span>London</span><span class="locations__dot"></span>
      <span>Carmel Valley California:</span>
    </div>
    <div class="footer-mark">HALDEN</div>
  </section>

  <section class="sheet sheet--back" aria-label="Letterhead back">
    <div class="brand back__brand">
      <div class="brand__name">HALDEN</div>
      <div class="brand__tagline">Real Estate Investment &amp; Management</div>
    </div>
  </section>

</body>
</html>
```